Harbor Motor Website

We need a Wordpress site designed for a local automotive repair facility. Our goals for the website are the following:
-"Humanize" the business by showing our people and location (building).
-Communicate our "Local / Community" orientation (not a national chain store)
-Above the fold call to action(s). Online Appointment Schedule, Loaner Car Reservation and Chat Feature.
-Business Strengthening by showing industry affiliations.
Our corporate colors are: Blue Pantone 293 and Light Grey 427. Accent colors are Yellow Pantone 123 and Lime Green (lots of colors i know)
We have been trying to develop a site similar to this site: www.brightlanegarage.com. I like the header image(s). I believe this site reinforces local ownership and conveys trust.
We built this site to try and duplicate but I do not like the results:
http://pelvistudio.com/harbor2/
This is our current site: www.harbormotorrepairplace.com
My SEO firm would like you to adhere to the following:
Here are the basics:
+ Full width of site 1080px, centered
+ Header no taller than 300px
+ Need standard selection of pages, including a full page layout
+ On pages with a sidebar, main column width at least 640px, sidebar 320px
+ All page titles should be an H1, and the only H1 on the page
+ Provide 4 footer widgets spanning the width of the site
Images are uploaded. Please let me know if there are additional images or direction needed.
Thanks,
Martin Kovacs
I have made committed on the payment for this project. I am looking forward to seeing some great WordPress designs.
Thank you,
Martin
I have uploaded an image of a Postcard that we send out in our local area. Many of our print materials carry this type of look and feel.
I HESITATED to upload this because I do not want to "stifle" or "steer" your creativity. I thought you may be able to pull some elements out of this for consistency. It is alright if you choose a different direction with your graphic elements.
Thanks,
Martin
First off, thanks for all the great work. Make sure you get your final ideas uploaded by the deadline (tomorrow).
I will take a few days to review, get feedback from my colleges and then make a final selection.
Your hard work is appreciated.
Sincerely,
Martin
Target Market(s)
35-60 years old with an even mix of male and female.
Upper income demographic who are driving 2+ vehicles in the household that are 3 years or older.
Industry/Entity Type
Automotive
Look and feel

```html
<!DOCTYPE html>
<html lang="en">
<head>
<meta charset="utf-8">
<title>Harbor Motor Repair</title>
<link rel="stylesheet" href="https://fonts.googleapis.com/css2?family=Ubuntu:wght@400;500;700&family=Open+Sans:wght@400;600;700&display=swap">
<style>
:root{
  --navy:#0d1f80;
  --navy-dark:#081560;
  --yellow:#f4b400;
  --yellow-light:#f9cf3c;
  --grey:#ececec;
  --text:#333;
  --footer:#262626;
  --white:#fff;
}
*{box-sizing:border-box;margin:0;padding:0}
html,body{width:1200px;height:2240px;overflow:hidden}
body{position:relative;background:var(--white);font-family:"Open Sans",Arial,sans-serif;color:var(--text);font-size:12px}
.abs{position:absolute}
h1,h2,h3{font-family:"Ubuntu",Arial,sans-serif}

/* top bar */
.top-bar{left:0;top:0;width:1200px;height:35px;background:var(--white)}
.top-phone{left:838px;top:6px;display:flex;align-items:center;gap:8px;font-family:"Ubuntu",sans-serif;font-size:20px;color:var(--navy)}

/* header */
.site-header{left:0;top:35px;width:1200px;height:120px;background:linear-gradient(var(--navy),var(--navy-dark))}
.header-rule{left:0;top:155px;width:1200px;height:10px;background:var(--yellow)}
.brand{left:187px;top:55px;width:235px;height:100px;display:flex;align-items:center;gap:12px}
.brand-mark{width:22px;height:22px;border-radius:50%;background:var(--yellow)}
.brand-name{font-family:"Ubuntu",sans-serif;font-weight:700;font-size:30px;color:var(--white);line-height:1}
.appointment-btn{left:745px;top:72px;width:268px;height:58px;background:var(--white);border-radius:4px;display:flex;align-items:center;padding-left:8px}
.appointment-btn span{font-family:"Ubuntu",sans-serif;font-weight:700;font-size:20px;color:var(--navy)}
.appointment-icon{position:absolute;right:-6px;top:-6px;width:70px;height:70px;border-radius:50%;background:var(--yellow);border:4px solid var(--white);display:flex;align-items:center;justify-content:center}

/* nav */
.main-nav{left:0;top:165px;width:1200px;height:50px;background:linear-gradient(#f7f7f7,#e2e2e2)}
.main-nav ul{position:absolute;left:190px;top:0;display:flex;list-style:none;height:50px}
.main-nav li{height:50px;line-height:50px;padding:0 22px;font-size:14px;color:#444;border-right:1px solid #d0d0d0}
.main-nav li.active{background:var(--yellow);color:var(--white)}

/* hero */
.hero{left:0;top:215px;width:1200px;height:355px;background:linear-gradient(#6f86a6 0%,#a9b3bc 45%,#6d5b4b 75%,#3d3a36 100%)}
.hero-caption{left:0;top:520px;width:1200px;height:50px;background:rgba(0,0,0,.55)}
.hero-caption p{position:absolute;left:190px;top:10px;color:var(--white);font-family:"Ubuntu",sans-serif}
.hero-caption b{font-size:24px;font-weight:500;letter-spacing:.3px}
.hero-caption span{font-size:16px;margin-left:12px}
.hero-arrow{width:40px;height:40px;border-radius:50%;background:rgba(255,255,255,.35);display:flex;align-items:center;justify-content:center}
.dots{left:580px;top:580px;display:flex;gap:5px}
.dots i{width:11px;height:11px;border-radius:50%;border:1px solid #999;background:var(--white)}
.dots i.on{background:var(--navy);border-color:var(--navy)}

/* welcome */
.cta-card{left:187px;width:275px;height:95px;background:var(--navy);border-radius:3px;box-shadow:0 6px 6px -4px rgba(0,0,0,.35)}
.cta-card h3{position:absolute;left:14px;top:16px;width:150px;color:var(--white);font-size:17px;font-weight:500;line-height:1.25}
.cta-img{position:absolute;right:10px;top:32px;width:98px;height:40px;border-radius:18px 18px 8px 8px;background:linear-gradient(#f0f3f6,#b8c2cc)}
.cta-gauge{position:absolute;right:22px;top:16px;width:62px;height:62px;border-radius:50%;border:4px solid var(--white);display:flex;align-items:center;justify-content:center}
.welcome-title{left:497px;top:628px;font-size:26px;font-weight:500;color:var(--navy);white-space:nowrap}
.welcome-text{left:497px;top:670px;width:362px;font-size:10.5px;line-height:17px;color:#444}
.welcome-text p+p{margin-top:16px}
.welcome-text .view-more{margin-top:6px;text-align:right;font-size:11px;color:var(--navy);font-weight:600}
.owner-photo{left:880px;top:662px;width:125px;height:180px;border-radius:62px 62px 10px 10px;background:linear-gradient(#e4e7ea,#8b96a3)}

/* oil band */
.oil-band{left:0;top:935px;width:1200px;height:215px;background:linear-gradient(100deg,var(--yellow) 0%,var(--yellow-light) 50%,#e7a400 100%)}
.oil-photo{left:687px;top:940px;width:325px;height:210px;border-radius:110px 0 0 0;background:linear-gradient(120deg,#5a6878,#9aa8b6 55%,#c74c4c 100%)}
.oil-title{left:190px;top:958px;color:var(--white);font-family:"Ubuntu",sans-serif}
.oil-title b{font-size:28px;font-weight:700}
.oil-title span{font-size:14px;font-weight:700;margin-left:8px}
.oil-text{left:190px;top:1004px;width:480px;font-size:10px;line-height:14px;color:#4a3500}
.oil-text p+p{margin-top:10px}
.oil-call{left:190px;top:1090px;color:var(--white);font-family:"Ubuntu",sans-serif}
.oil-call b{font-size:20px}
.oil-call span{font-size:30px;margin-left:8px}

/* sidebar */
.side-head{left:187px;width:275px;height:42px;background:var(--navy);color:var(--white);font-family:"Ubuntu",sans-serif;font-size:20px;font-weight:500;padding:8px 12px;box-shadow:0 6px 6px -4px rgba(0,0,0,.35)}
.side-list{left:187px;width:275px;list-style:none}
.side-list li{font-size:10.5px;color:#333;height:25px;line-height:25px;border-bottom:1px solid #ddd;padding-left:12px;position:relative;text-transform:uppercase}
.side-list li::before{content:"";position:absolute;left:2px;top:10px;border:3px solid transparent;border-left-color:#444}
.side-list.plain li{text-transform:none;font-size:11.5px;border:none;height:24px;line-height:24px}

/* services */
.svc-head{left:497px;top:1200px;width:515px;height:42px;background:var(--navy);color:var(--white);font-family:"Ubuntu",sans-serif;font-size:20px;font-weight:500;padding:8px 14px;box-shadow:0 6px 6px -4px rgba(0,0,0,.35)}
.view-all{left:945px;top:1180px;width:68px;height:68px;border-radius:50%;background:var(--yellow);border:4px solid var(--white);color:var(--white);font-size:13px;text-align:center;padding-top:14px;line-height:1.2;box-shadow:0 2px 4px rgba(0,0,0,.3)}
.timeline{left:748px;top:1268px;width:4px;height:325px;background:var(--navy)}
.svc-icon{width:66px;height:66px;border-radius:50%;background:var(--navy);display:flex;align-items:center;justify-content:center}
.svc-line{height:3px;background:var(--navy)}
.svc-label{font-size:12.5px;color:var(--navy);white-space:nowrap}

/* affiliations */
.affil{left:0;top:1685px;width:1200px;height:205px;background:var(--grey)}
.affil-title{left:0;top:1712px;width:1200px;text-align:center;font-size:30px;font-weight:500;color:var(--navy)}
.affil-rule{top:1735px;height:2px;width:160px;background:#bbb}
.badge{top:1790px;height:60px;border-radius:6px}
.affil-arrow{top:1792px}

/* footer */
.site-footer{left:0;top:1890px;width:1200px;height:305px;background:var(--footer)}
.foot-col{top:1925px;width:190px}
.foot-col h4{font-family:"Ubuntu",sans-serif;font-size:16px;color:var(--yellow);font-weight:500;margin-bottom:8px}
.foot-col ul{list-style:none}
.foot-col li{font-size:12px;color:#cfcfcf;line-height:23px;border-bottom:1px solid #3a3a3a;padding-left:10px;position:relative}
.foot-col li::before{content:"";position:absolute;left:0;top:10px;width:4px;height:4px;background:var(--yellow);border-radius:50%}
.contact-row{display:flex;gap:10px;font-size:11.5px;color:#cfcfcf;margin-bottom:14px;line-height:1.4}
.social{display:flex;gap:12px;margin-top:14px}
.social i{width:14px;height:14px;border-radius:50%;background:var(--yellow)}
.news-text{font-size:11.5px;color:#bbb;line-height:1.4}
.news-input{margin-top:12px;width:195px;height:32px;background:var(--white);font-size:11px;color:#999;padding:8px}
.news-btn{margin-top:12px;width:75px;height:30px;background:var(--yellow);color:var(--white);font-size:12px;font-weight:700;text-align:center;line-height:30px}
.copyright{left:0;top:2195px;width:1200px;height:45px;background:var(--navy);color:#c9d0ef;font-size:11px;text-align:center;line-height:45px}
</style>
</head>
<body>

<div class="abs top-bar"></div>
<div class="abs top-phone">
  <svg width="22" height="22" viewBox="0 0 22 22"><circle cx="11" cy="11" r="10" fill="none" stroke="#0d1f80" stroke-width="2"/><path d="M7 6l2 0 1 3-1.5 1a7 7 0 0 0 3.5 3.5l1-1.5 3 1v2a1 1 0 0 1-1 1A10 10 0 0 1 6 7a1 1 0 0 1 1-1z" fill="#0d1f80"/></svg>
  (602) 555-0187
</div>

<header class="abs site-header"></header>
<div class="abs header-rule"></div>
<div class="abs brand"><span class="brand-mark"></span><span class="brand-name">Harbor Motor</span></div>
<div class="abs appointment-btn"><span>Online Appointment</span>
  <div class="appointment-icon"><svg width="30" height="30" viewBox="0 0 30 30"><rect x="3" y="6" width="24" height="21" rx="2" fill="#fff"/><rect x="3" y="6" width="24" height="6" fill="#0d1f80"/><rect x="8" y="2" width="3" height="7" fill="#fff"/><rect x="19" y="2" width="3" height="7" fill="#fff"/></svg></div>
</div>

<nav class="abs main-nav"><ul>
  <li class="active">Home</li><li>Stuff</li><li>Junk</li><li>Contact</li><li>About</li><li>Auto Repair</li><li>Loaner Cars</li><li>Free</li><li>Shuttle Info</li>
</ul></nav>

<div class="abs hero" role="img" aria-label="Photo of the Harbor Motor Repair shop building at dusk with parked cars"></div>
<div class="abs hero-caption"><p><b>PROFESSIONALS THAT KNOW CARS</b><span>Knowledge &amp; Experience, you can Trust</span></p></div>
<div class="abs hero-arrow" style="left:185px;top:368px"><svg width="14" height="14" viewBox="0 0 14 14"><path d="M9 2L4 7l5 5" stroke="#fff" stroke-width="2.5" fill="none"/></svg></div>
<div class="abs hero-arrow" style="left:973px;top:368px"><svg width="14" height="14" viewBox="0 0 14 14"><path d="M5 2l5 5-5 5" stroke="#fff" stroke-width="2.5" fill="none"/></svg></div>
<div class="abs dots"><i class="on"></i><i></i><i></i></div>

<div class="abs cta-card" style="top:635px"><h3>Request a Loaner Vehicle</h3><div class="cta-img" role="img" aria-label="White loaner car"></div></div>
<div class="abs cta-card" style="top:765px"><h3>Fusce interdum est et tristique suscipit</h3>
  <div class="cta-gauge"><svg width="34" height="34" viewBox="0 0 34 34"><circle cx="17" cy="17" r="3" fill="#fff"/><path d="M17 17L26 9" stroke="#fff" stroke-width="3"/><path d="M5 22a12 12 0 1 1 24 0" stroke="#fff" stroke-width="2" fill="none"/></svg></div>
</div>

<h1 class="abs welcome-title">WELCOME TO HARBOR MOTOR REPAIR</h1>
<div class="abs welcome-text">
  <p>What sets our Westbrook auto repair shop apart from the competition is our high level of competency as an automotive repair shop. When you need a car repair shop with qualified mechanics that can handle the toughest auto service and repair jobs, your search ends with us, whether you're in the Westbrook, Millbrook or Redfield area.</p>
  <p>Our Westbrook car repair center is a full service automotive repair shop with a strong track record in the performance of complex auto service and repair work. Many times those are services other auto repair shops in town wouldn't dream of taking on.</p>
  <p class="view-more">View more »</p>
</div>
<div class="abs owner-photo" role="img" aria-label="Portrait of the shop owner"></div>

<section class="abs oil-band"></section>
<div class="abs oil-photo" role="img" aria-label="Mechanic handing keys to a smiling customer"></div>
<h2 class="abs oil-title"><b>OIL CHANGE SERVICES</b><span>Service Department Special</span></h2>
<div class="abs oil-text">
  <p>Nunc interdum, lacus sit amet iaculis malesuada, felis urna mollis neque, elementum euismod est neque id lorem. Cras ullamcorper tortor ac cursus molestie.</p>
  <p>Aliquam interdum sodales eros non mollis. Curabitur vitae elit eget dolor ullamcorper consectetur. Pellentesque habitant morbi tristique senectus et netus et malesuada.</p>
</div>
<div class="abs oil-call"><b>Call Us Today</b><span>(602) 555-0187</span></div>

<div class="abs side-head" style="top:1200px">Our Automotive Menu</div>
<ul class="abs side-list" style="top:1252px">
  <li>Auto Repair Services</li><li>Car Repair Coupons</li><li>Our Customers Speak</li><li>Auto Repair Blog</li><li>About Us</li><li>Contact Us + Directions</li>
</ul>
<div class="abs side-head" style="top:1430px">Sed ac auctor nisi</div>
<ul class="abs side-list plain" style="top:1495px">
  <li>Fusce suscipit justo nibh</li><li>Sed ornare diam volutpat id. Aenean mattis</li><li>Tellus nunc, eu suscipit urna scelerisque et</li><li>Nulla feugiat dolor quis metus volutpat</li>
</ul>

<div class="abs svc-head">We Offers the Following Automotive Services</div>
<div class="abs view-all">View<br>All</div>
<div class="abs timeline"></div>

<div class="abs svc-line" style="left:608px;top:1317px;width:140px"></div>
<div class="abs svc-icon" style="left:575px;top:1284px"><svg width="34" height="34" viewBox="0 0 34 34"><rect x="6" y="5" width="22" height="20" rx="3" fill="#fff"/><rect x="9" y="8" width="16" height="7" fill="#0d1f80"/><circle cx="11" cy="28" r="2.5" fill="#fff"/><circle cx="23" cy="28" r="2.5" fill="#fff"/></svg></div>
<div class="abs svc-label" style="left:525px;top:1358px">Shuttle Service</div>

<div class="abs svc-line" style="left:640px;top:1420px;width:108px"></div>
<div class="abs svc-icon" style="left:575px;top:1387px"><svg width="36" height="36" viewBox="0 0 36 36"><path d="M6 20l4-8h16l4 8v7H6z" fill="#fff"/><circle cx="11" cy="27" r="3" fill="#0d1f80" stroke="#fff" stroke-width="2"/><circle cx="25" cy="27" r="3" fill="#0d1f80" stroke="#fff" stroke-width="2"/></svg></div>
<div class="abs svc-label" style="left:525px;top:1461px">General Auto Repair &amp; Maintenance</div>

<div class="abs svc-line" style="left:640px;top:1522px;width:108px"></div>
<div class="abs svc-icon" style="left:575px;top:1490px"><svg width="34" height="34" viewBox="0 0 34 34"><circle cx="17" cy="17" r="9" fill="none" stroke="#fff" stroke-width="5" stroke-dasharray="4 3"/><circle cx="17" cy="17" r="4" fill="#fff"/></svg></div>
<div class="abs svc-label" style="left:525px;top:1564px">Transmission Repair &amp; Replacement</div>

<div class="abs svc-line" style="left:752px;top:1362px;width:118px"></div>
<div class="abs svc-icon" style="left:870px;top:1330px"><svg width="34" height="34" viewBox="0 0 34 34"><g stroke="#fff" stroke-width="3"><path d="M17 4v26M5 10l24 14M5 24l24-14"/></g><circle cx="17" cy="17" r="4" fill="#fff"/></svg></div>
<div class="abs svc-label" style="left:845px;top:1404px">Air Conditioning A/C Repair</div>

<div class="abs svc-line" style="left:752px;top:1467px;width:118px"></div>
<div class="abs svc-icon" style="left:870px;top:1435px"><svg width="34" height="34" viewBox="0 0 34 34"><circle cx="17" cy="17" r="13" fill="none" stroke="#fff" stroke-width="5"/><circle cx="17" cy="17" r="4" fill="#fff"/></svg></div>
<div class="abs svc-label" style="left:840px;top:1509px">Tire Repair and Replacement</div>

<div class="abs svc-line" style="left:752px;top:1567px;width:118px"></div>
<div class="abs svc-icon" style="left:870px;top:1535px"><svg width="30" height="30" viewBox="0 0 30 30"><rect x="6" y="5" width="13" height="21" rx="2" fill="#fff"/><rect x="9" y="8" width="7" height="5" fill="#0d1f80"/><path d="M19 10l4 3v9a2 2 0 0 0 2 0V12" stroke="#fff" stroke-width="2" fill="none"/></svg></div>
<div class="abs svc-label" style="left:898px;top:1611px">Fuel System Repair</div>

<section class="abs affil"></section>
<div class="abs affil-rule" style="left:245px"></div>
<div class="abs affil-rule" style="left:795px"></div>
<h2 class="abs affil-title">INDUSTRY AFFILIATIONS</h2>
<svg class="abs affil-arrow" style="left:187px" width="22" height="56" viewBox="0 0 22 56"><path d="M18 2L4 28l14 26" stroke="#0d1f80" stroke-width="4" fill="none"/></svg>
<svg class="abs affil-arrow" style="left:990px" width="22" height="56" viewBox="0 0 22 56"><path d="M4 2l14 26L4 54" stroke="#0d1f80" stroke-width="4" fill="none"/></svg>
<div class="abs badge" style="left:225px;width:140px;background:#1f4e8c"></div>
<div class="abs badge" style="left:385px;width:125px;background:#cfd3d8"></div>
<div class="abs badge" style="left:530px;width:130px;background:#c9c9c9"></div>
<div class="abs badge" style="left:690px;width:125px;background:#d0202a;border-radius:30px"></div>
<div class="abs badge" style="left:840px;width:135px;background:#1a3f8f"></div>

<footer class="abs site-footer"></footer>
<div class="abs foot-col" style="left:192px"><h4>Site map</h4><ul>
  <li>Home</li><li>Stuff</li><li>Junk</li><li>Contact</li><li>About</li><li>Auto Repair</li><li>Loaner Car</li><li>Shuttle Info</li></ul></div>
<div class="abs foot-col" style="left:402px"><h4>Quick Links</h4><ul>
  <li>Ut pellentesque lorem</li><li>porttitor justo</li><li>fermentum, et iaculis</li><li>orci tempus. Donec</li><li>orci leo, hendrerit ut</li><li>vulputate et, iaculis sit</li><li>amet leo. Aliquam nec</li><li>dui ornare, mollis elit</li></ul></div>
<div class="abs foot-col" style="left:612px"><h4>Contact Info</h4>
  <div class="contact-row"><svg width="14" height="14" viewBox="0 0 14 14"><path d="M1 7l6-5 6 5v6H1z" fill="#fff"/></svg><span>345 - Etiam eu felis quis lectus hendrerit suscipit</span></div>
  <div class="contact-row"><svg width="14" height="14" viewBox="0 0 14 14"><path d="M3 1h3l1 3-2 1a7 7 0 0 0 4 4l1-2 3 1v3a1 1 0 0 1-1 1A12 12 0 0 1 2 2a1 1 0 0 1 1-1z" fill="#fff"/></svg><span>(602) 555-0187</span></div>
  <div class="contact-row"><svg width="14" height="14" viewBox="0 0 14 14"><rect x="1" y="3" width="12" height="8" fill="#fff"/><path d="M1 3l6 5 6-5" stroke="#262626" fill="none"/></svg><span>info@harbormotorrepair.com</span></div>
  <h4 style="margin-top:14px">Get social</h4>
  <div class="social"><i></i><i></i><i></i><i></i></div>
</div>
<div class="abs foot-col" style="left:817px;width:200px"><h4>Subscribe Newsletter</h4>
  <p class="news-text">Curabitur tempor placerat fermentum. Sed vehicula ultricies urna dolor.</p>
  <div class="news-input">Enter email address</div>
  <div class="news-btn">Submit</div>
</div>
<div class="abs copyright">Copyright 2016 All rights reserved</div>

</body>
</html>
```